Corvane Supplies Business Card

Professional business card that stand out to our potential customers. Front and back with clean modern design

Industry/Entity Type

Oil and gas

Contact Information for Business Card

Name, address, website , office phone and cell number

Requirements
Must have
• Editable files for each employee

```html
<!DOCTYPE html>
<html lang="en">
<head>
<meta charset="utf-8">
<title>Corvane Supplies Business Card</title>
<link href="https://fonts.googleapis.com/css2?family=Roboto:wght@400;700;900&display=swap" rel="stylesheet">
<style>
  :root {
    --stage: #5c5c5e;
    --card-dark: #1e1e1f;
    --card-dark-edge: #2a2a2b;
    --card-light: #ffffff;
    --brand-red: #e41e24;
    --brand-blue: #00a8d0;
    --ink: #1f1f1f;
  }
  * { margin: 0; padding: 0; box-sizing: border-box; }
  html, body { width: 900px; height: 1200px; overflow: hidden; }
  body {
    background: var(--stage);
    font-family: "Roboto", Arial, sans-serif;
    position: relative;
  }
  .card {
    position: absolute;
    left: 134px;
    width: 632px;
    height: 364px;
    overflow: hidden;
  }
  .card-front { top: 210px; background: var(--card-dark); }
  .card-back { top: 624px; background: var(--card-light); }

  .front-texture {
    position: absolute; inset: 0;
    background: radial-gradient(ellipse at 70% 30%, var(--card-dark-edge), var(--card-dark) 70%);
  }
  .front-brand {
    position: absolute;
    left: 0; right: 0; top: 168px;
    display: flex; align-items: center; justify-content: center; gap: 12px;
  }
  .brand-mark { width: 22px; height: 22px; background: var(--brand-red); }
  .brand-name {
    font-weight: 900;
    font-size: 26px;
    letter-spacing: 0.5px;
    text-transform: uppercase;
  }
  .front-brand .brand-name { color: #ffffff; }

  .back-brand {
    position: absolute;
    left: 40px; width: 250px; top: 158px;
    display: flex; align-items: center; justify-content: center; gap: 10px;
  }
  .back-brand .brand-mark { width: 18px; height: 18px; }
  .back-brand .brand-name { font-size: 20px; color: var(--brand-red); }

  .divider { position: absolute; left: 316px; width: 2px; }
  .divider-top { top: 100px; height: 37px; background: var(--brand-red); }
  .divider-mid { top: 139px; height: 89px; background: var(--brand-blue); }
  .divider-bottom { top: 232px; height: 37px; background: var(--brand-red); }

  .contact { position: absolute; left: 346px; top: 96px; color: var(--ink); }
  .person-name { font-weight: 700; font-size: 25px; line-height: 30px; }
  .person-name .first { color: var(--brand-red); }
  .person-name .last { color: var(--brand-blue); }
  .person-role { font-size: 15px; line-height: 18px; margin-top: 0; }
  .address { font-size: 15px; line-height: 21px; margin-top: 6px; }
  .contact-list { list-style: none; margin-top: 5px; }
  .contact-list li {
    display: flex; align-items: center; gap: 8px;
    font-size: 15px; line-height: 25.5px;
  }
  .contact-list svg { width: 15px; height: 15px; fill: var(--brand-blue); flex: none; }
  .phone-number { letter-spacing: 2.5px; }

  .base-band { position: absolute; left: 0; bottom: 0; width: 632px; height: 13px; }
</style>
</head>
<body>

<section class="card card-front">
  <div class="front-texture" role="img" aria-label="Faint embossed repeating brand monogram pattern on dark stock"></div>
  <div class="front-brand">
    <span class="brand-mark"></span>
    <span class="brand-name">Corvane Supplies</span>
  </div>
</section>

<section class="card card-back">
  <div class="back-brand">
    <span class="brand-mark"></span>
    <span class="brand-name">Corvane Supplies</span>
  </div>

  <span class="divider divider-top"></span>
  <span class="divider divider-mid"></span>
  <span class="divider divider-bottom"></span>

  <div class="contact">
    <h1 class="person-name"><span class="first">Ravin</span> <span class="last">Desai</span></h1>
    <p class="person-role">CEO</p>
    <p class="address">412 N.Larkfield Suite 7<br>Midvale, Tx 79700</p>
    <ul class="contact-list">
      <li>
        <svg viewBox="0 0 24 24" aria-hidden="true"><path d="M6.6 10.8a15.1 15.1 0 0 0 6.6 6.6l2.2-2.2a1 1 0 0 1 1-.25 11.4 11.4 0 0 0 3.6.57 1 1 0 0 1 1 1V20a1 1 0 0 1-1 1A17 17 0 0 1 3 4a1 1 0 0 1 1-1h3.5a1 1 0 0 1 1 1c0 1.25.2 2.45.57 3.57a1 1 0 0 1-.25 1z"/></svg>
        <span class="phone-number">(555)014-2738</span>
      </li>
      <li>
        <svg viewBox="0 0 24 24" aria-hidden="true"><path d="M2 5h20v14H2z" fill="none"/><path d="M2 5h20L12 13z"/><path d="M2 7l10 8 10-8v12H2z"/></svg>
        <span>sales@corvanesupplies.com</span>
      </li>
      <li>
        <svg viewBox="0 0 24 24" aria-hidden="true"><path d="M12 2a10 10 0 1 0 0 20 10 10 0 0 0 0-20zm6.9 6h-2.9a15 15 0 0 0-1.4-3.6A8 8 0 0 1 18.9 8zM12 4c.8 1.2 1.5 2.5 1.9 4h-3.8c.4-1.5 1.1-2.8 1.9-4zM4.3 14a8 8 0 0 1 0-4h3.4a16 16 0 0 0 0 4zm.8 2h2.9c.3 1.3.8 2.5 1.4 3.6A8 8 0 0 1 5.1 16zM8 8H5.1a8 8 0 0 1 4.3-3.6C8.8 5.5 8.3 6.7 8 8zm4 12c-.8-1.2-1.5-2.5-1.9-4h3.8c-.4 1.5-1.1 2.8-1.9 4zm2.3-6H9.7a14 14 0 0 1 0-4h4.6a14 14 0 0 1 0 4zm.3 5.6c.6-1.1 1.1-2.3 1.4-3.6h2.9a8 8 0 0 1-4.3 3.6zm1.7-5.6a16 16 0 0 0 0-4h3.4a8 8 0 0 1 0 4z"/></svg>
        <span>www.corvanesupplies.com</span>
      </li>
    </ul>
  </div>

  <svg class="base-band" viewBox="0 0 632 13" preserveAspectRatio="none" aria-hidden="true">
    <polygon points="0,0 325,0 321,13 0,13" fill="var(--brand-red)"/>
    <polygon points="328,0 632,0 632,13 324,13" fill="var(--brand-blue)"/>
  </svg>
</section>

</body>
</html>
```